Stationery Design needed for logo design project

This company needs a letterhead and envelope for their new practice. We did not want to release this contact until the business card design was finalized so the stationary can be created to coordinate with it.

For those of you that will be submitting designs for this content, think "linear". Designs with curves or "swooshes" are not appropriate for this design.

NOTE: As part of the source files; I will require FULLY LAYERED PHOTOSHOP FILES of all elements, including design elements, text and fonts. If you cannot provide a fully layered PSD file, please do not submit.
Updates

The project details have been updated. We have added a new description along with logo files and business card design. Please review the style of the logo and business card before submitting designs. Thanks

Target Market(s)

Medical

Industry/Entity Type

Business

Requirements
Must have
• NOTE: As part of the source files; I will require FULLY LAYERED PHOTOSHOP FILES of all elements, including design elements, text and fonts. If you cannot provide a fully layered PSD file, please do not submit.

Logo
2 office address locations
phone
fax
email
website URL

```html
<!DOCTYPE html>
<html lang="en">
<head>
<meta charset="utf-8">
<title>Delmar &amp; Associates — Stationery Set</title>
<link href="https://fonts.googleapis.com/css2?family=Lato:wght@400;700&display=swap" rel="stylesheet">
<style>
  :root {
    --backdrop: #ececec;
    --paper: #ffffff;
    --brand-red: #a81f24;
    --ink: #111111;
    --text-grey: #4a4a4a;
    --rule: #d9a3a5;
  }
  * { box-sizing: border-box; margin: 0; padding: 0; }
  html, body { width: 1200px; height: 800px; overflow: hidden; }
  body {
    background: var(--backdrop);
    font-family: "Lato", Arial, sans-serif;
    color: var(--text-grey);
    position: relative;
  }
  .sheet {
    position: absolute;
    background: var(--paper);
    overflow: hidden;
  }

  /* Brand name block */
  .brand {
    position: absolute;
    display: flex;
    align-items: center;
    gap: 7px;
  }
  .brand__dot {
    border-radius: 50%;
    background: var(--brand-red);
    flex: none;
  }
  .brand__name {
    font-family: "Lato", Arial, sans-serif;
    font-weight: 400;
    color: var(--ink);
    text-transform: uppercase;
    letter-spacing: 0.04em;
    white-space: nowrap;
  }

  /* Contact footer */
  .contact {
    position: absolute;
    display: flex;
    line-height: 1.28;
    color: var(--text-grey);
  }
  .contact__col { padding-right: 6px; }
  .contact__col + .contact__col {
    border-left: 1px solid var(--rule);
    padding-left: 6px;
  }
  .contact__label { color: var(--brand-red); font-weight: 700; }
  .contact__line { display: flex; align-items: center; gap: 3px; white-space: nowrap; }
  .contact__line svg { flex: none; }
  .contact__col div { white-space: nowrap; }

  .base-band { position: absolute; left: 0; bottom: 0; }

  /* Letterhead */
  .letterhead { left: 186px; top: 126px; width: 403px; height: 552px; }
  .letterhead .brand { left: 22px; top: 26px; }
  .letterhead .brand__dot { width: 14px; height: 14px; }
  .letterhead .brand__name { font-size: 17px; }
  .letterhead .contact { left: 23px; top: 495px; font-size: 6.4px; }

  /* Business cards */
  .card { top: 130px; width: 156px; height: 90px; }
  .card--front { left: 634px; }
  .card--back { left: 852px; }
  .card .brand { left: 18px; top: 37px; }
  .card .brand__dot { width: 8px; height: 8px; }
  .card .brand__name { font-size: 9.5px; }

  /* Compliment slip */
  .slip { left: 634px; top: 267px; width: 381px; height: 190px; }
  .slip .brand { left: 16px; top: 34px; }
  .slip .brand__dot { width: 13px; height: 13px; }
  .slip .brand__name { font-size: 15.5px; }
  .slip .contact { left: 18px; top: 139px; font-size: 6px; }

  /* Envelope */
  .envelope { left: 636px; top: 484px; width: 383px; height: 193px; }
  .envelope__flap { position: absolute; left: 0; top: 0; }
  .envelope .brand {
    left: 0; right: 0; top: 20px;
    justify-content: center;
  }
  .envelope .brand__dot { width: 9px; height: 9px; background: var(--paper); }
  .envelope .brand__name { font-size: 11px; color: var(--paper); }
</style>
</head>
<body>

  <!-- Letterhead -->
  <section class="sheet letterhead">
    <div class="brand">
      <span class="brand__dot"></span>
      <span class="brand__name">Delmar &amp; Associates</span>
    </div>

    <div class="contact">
      <div class="contact__col">
        <div class="contact__line">
          <svg width="6" height="6" viewBox="0 0 10 10"><path d="M2 1l2 2-1 1.5a6 6 0 0 0 2.5 2.5L7 6l2 2-1.5 1.5C4 9 1 6 .5 2.5z" fill="var(--brand-red)"/></svg>
          (555) 240-1187
        </div>
        <div class="contact__line">
          <svg width="6" height="6" viewBox="0 0 10 10"><rect x="2" y="0.5" width="6" height="3" fill="var(--brand-red)"/><rect x="0.5" y="4" width="9" height="5" rx="1" fill="var(--brand-red)"/></svg>
          (555) 240-1188
        </div>
        <div class="contact__line">
          <svg width="6" height="6" viewBox="0 0 10 10"><rect x="0.5" y="2" width="9" height="6" fill="var(--brand-red)"/><path d="M.5 2l4.5 3.5L9.5 2" stroke="#fff" fill="none"/></svg>
          info@delmarheart.com
        </div>
        <div class="contact__line">
          <svg width="6" height="6" viewBox="0 0 10 10"><circle cx="5" cy="5" r="4.5" fill="var(--brand-red)"/><path d="M.5 5h9M5 .5v9" stroke="#fff" stroke-width="0.8"/></svg>
          www.delmarheart.com
        </div>
      </div>
      <div class="contact__col">
        <div class="contact__label">Downtown Office:</div>
        <div>412 Alder Ct NE</div>
        <div>Suite 6, Ridgeford, OR 97310</div>
        <div>Phone: (555) 310-4420</div>
      </div>
      <div class="contact__col">
        <div class="contact__label">West Side Office:</div>
        <div>88 Harlan Way SE</div>
        <div>Suite 9, Fairview, OR 97342</div>
        <div>Phone: (555) 310-4420</div>
      </div>
    </div>

    <svg class="base-band" width="403" height="18" viewBox="0 0 403 18">
      <rect x="0" y="6" width="403" height="12" fill="var(--brand-red)"/>
      <path d="M236 18 L239 4 Q240 0 245 0 L403 0 L403 18 Z" fill="var(--paper)"/>
      <path d="M239 18 L242 6 Q243 2 248 2 L403 2 L403 18 Z" fill="var(--ink)"/>
    </svg>
  </section>

  <!-- Business card, front -->
  <section class="sheet card card--front">
    <div class="brand">
      <span class="brand__dot"></span>
      <span class="brand__name">Delmar &amp; Associates</span>
    </div>
  </section>

  <!-- Business card, back -->
  <section class="sheet card card--back">
    <div class="brand">
      <span class="brand__dot"></span>
      <span class="brand__name">Delmar &amp; Associates</span>
    </div>
  </section>

  <!-- Compliment slip -->
  <section class="sheet slip">
    <div class="brand">
      <span class="brand__dot"></span>
      <span class="brand__name">Delmar &amp; Associates</span>
    </div>

    <div class="contact">
      <div class="contact__col">
        <div class="contact__line">
          <svg width="6" height="6" viewBox="0 0 10 10"><path d="M2 1l2 2-1 1.5a6 6 0 0 0 2.5 2.5L7 6l2 2-1.5 1.5C4 9 1 6 .5 2.5z" fill="var(--brand-red)"/></svg>
          (555) 240-1187
        </div>
        <div class="contact__line">
          <svg width="6" height="6" viewBox="0 0 10 10"><rect x="2" y="0.5" width="6" height="3" fill="var(--brand-red)"/><rect x="0.5" y="4" width="9" height="5" rx="1" fill="var(--brand-red)"/></svg>
          (555) 240-1188
        </div>
        <div class="contact__line">
          <svg width="6" height="6" viewBox="0 0 10 10"><rect x="0.5" y="2" width="9" height="6" fill="var(--brand-red)"/><path d="M.5 2l4.5 3.5L9.5 2" stroke="#fff" fill="none"/></svg>
          info@delmarheart.com
        </div>
        <div class="contact__line">
          <svg width="6" height="6" viewBox="0 0 10 10"><circle cx="5" cy="5" r="4.5" fill="var(--brand-red)"/><path d="M.5 5h9M5 .5v9" stroke="#fff" stroke-width="0.8"/></svg>
          www.delmarheart.com
        </div>
      </div>
      <div class="contact__col">
        <div class="contact__label">Downtown Office:</div>
        <div>412 Alder Ct NE</div>
        <div>Suite 6, Ridgeford, OR 97310</div>
        <div>Phone: (555) 310-4420</div>
      </div>
      <div class="contact__col">
        <div class="contact__label">West Side Office:</div>
        <div>88 Harlan Way SE</div>
        <div>Suite 9, Fairview, OR 97342</div>
        <div>Phone: (555) 310-4420</div>
      </div>
    </div>

    <svg class="base-band" width="381" height="16" viewBox="0 0 381 16">
      <rect x="0" y="6" width="381" height="10" fill="var(--brand-red)"/>
      <path d="M213 16 L216 4 Q217 0 222 0 L381 0 L381 16 Z" fill="var(--paper)"/>
      <path d="M216 16 L219 6 Q220 2 225 2 L381 2 L381 16 Z" fill="var(--ink)"/>
    </svg>
  </section>

  <!-- Envelope -->
  <section class="sheet envelope">
    <svg class="envelope__flap" width="383" height="62" viewBox="0 0 383 62">
      <path d="M0 0 H383 L376 56 Q375 60 370 60 H13 Q8 60 7 56 Z" fill="var(--brand-red)"/>
    </svg>
    <div class="brand">
      <span class="brand__dot"></span>
      <span class="brand__name">Delmar &amp; Associates</span>
    </div>
  </section>

</body>
</html>
```